Cover for a book about building companies without hierarchy

We need to design the cover of our new book. In 2018 we have developed a new organizational design called "Brevunt" which mean equal, just in Latin. This organizational design is hierarchy-free, and it is formed by a radial network of self-organizing teams, where people can take decisions pertaining their job, be autonomous, and contribute to the well being of the larger organization. We published a book in 2018 (see the cover attached), titled: "Brevunt. The Open People-first Operating Model to Flourish in an Uncertain Age", where we used the graphic representation of the Brevunt structure in the cover (see attached). The book is intended for top managers, entrepreneurs, businesses.
After 5 years from its launch, we implemented this design in a number of companies and we learned a lot about what works and the challenges. So we decided to publish another book that will be titled: "Brevunt. 5 rules to build a people-first office" where we present a revised model, we focus on the principles behind Brevunt and we tell the story of the implementation of Brevunt in Caffora Italy.
The book cover design must include both front and back, using the template attached.
In the front we need to include: an image or illustration, the Names of the authors (Lucrezia Manfretti and Marcello Vagni) and the Quolvane logo.
In the back we shall include: an empty space for the ISDN code as in the template, a short description of the book, the pictures and short bios of the authors .
In the spine we shall include: the title and authors.
Here's the bios:
Lucrezia Manfretti is a partner at Quolvane, a global organizational development firm, a former executive in the corporate setting (including Brindle & Holloway and Zimbu! Inc.) and Past President of GTN Global (Global Tutoring Network). She is the author of the book “Inner Compass. The Road to Renewing Guidance” and a LUMIx speaker.
Marcello Vagni is a partner at Quolvane and a former manager in multinational settings. He is the co-author of the Keswick Management Quarterly articles “Why Your Inner Mood Shapes your Daily Output”, “3 Ways to Lift a Gloomy Day”, “Preparing Your Thoughts Properly for a Long Break” and “An Easy Method to Ease Lasting Tension”.
Pictures of the authors attached.
The final versions of the book cover shall be:
- book cover for paperback in English (front and back)
- Book cover for paperback in Italian (front and back)
- Book cover for kindle (only front)

```html
<!DOCTYPE html>
<html lang="en">
<head>
<meta charset="utf-8">
<title>Brevunt – Book Cover</title>
<link href="https://fonts.googleapis.com/css2?family=Catamaran:wght@400;500;700&family=Montserrat:wght@400&family=Saira+Condensed:wght@600&family=Saira+Semi+Condensed:wght@500&display=swap" rel="stylesheet">
<style>
  :root {
    --bg: #fbe9f3;
    --paper: #e9f4e8;
    --ink: #2f2d33;
    --title: #5a5361;
    --accent-blue: #3b87c4;
    --logo: #3f3a8c;
    --pink: #e83f8b;
    --green: #8cc84b;
    --orange: #f3a03a;
    --purple: #8e3f9c;
    --blue: #3a86c5;
  }
  * { margin: 0; padding: 0; box-sizing: border-box; }
  html, body { width: 1200px; height: 1200px; overflow: hidden; background: var(--bg); }
  .canvas { position: relative; width: 1200px; height: 1200px; }

  .cover {
    position: absolute; top: 222px; width: 540px; height: 756px;
    background: var(--paper); overflow: hidden;
    box-shadow: 0 12px 30px rgba(120, 60, 100, 0.18);
  }
  .cover--back { left: 34px; }
  .cover--front { left: 626px; }

  .spine-line { position: absolute; top: 0; bottom: 0; width: 6px;
    border-left: 1px solid rgba(0,0,0,0.06); border-right: 1px solid rgba(255,255,255,0.8); }
  .cover--back .spine-line { right: 30px; }
  .cover--front .spine-line { left: 30px; }

  .decor { position: absolute;
    background: linear-gradient(135deg, var(--green), var(--orange) 30%, var(--pink) 55%, var(--purple) 75%, var(--blue)); opacity: 0.85; }
  .decor--corner { left: -20px; top: -20px; width: 95px; height: 95px; border-radius: 0 0 40px 0; }
  .decor--edge { right: 0; top: 52px; width: 58px; height: 335px; border-radius: 30px 0 0 30px; }

  .blurb { position: absolute; left: 52px; top: 76px; width: 410px;
    font-family: "Catamaran", sans-serif; font-size: 12.6px; line-height: 21px; color: var(--ink); }
  .blurb p { margin-bottom: 11px; }

  .bio { position: absolute; left: 48px; width: 440px; }
  .bio--first { top: 370px; }
  .bio--second { top: 524px; }
  .bio__photo { position: absolute; left: 0; top: 0; width: 86px; height: 116px; }
  .bio__text { position: absolute; left: 100px; top: -6px; width: 345px;
    font-family: "Catamaran", sans-serif; font-size: 11.2px; line-height: 22px; color: var(--ink); }
  .bio__name { font-weight: 700; font-size: 12.6px; color: var(--accent-blue); }

  .title { position: absolute; left: 60px; right: 20px; top: 62px; text-align: center;
    font-family: "Saira Semi Condensed", sans-serif; font-weight: 500;
    font-size: 100px; line-height: 1; color: var(--title); letter-spacing: -1px; }
  .subtitle { position: absolute; left: 100px; right: 20px; top: 184px; text-align: center;
    font-family: "Saira Condensed", sans-serif; font-weight: 600;
    font-size: 26px; line-height: 38px; letter-spacing: 1.5px; color: var(--title); }
  .illustration { position: absolute; left: 0; top: 272px; width: 330px; height: 368px; }
  .authors { position: absolute; left: 150px; right: 20px; top: 652px; text-align: center;
    font-family: "Montserrat", sans-serif; font-size: 15.5px; line-height: 27px;
    letter-spacing: 0.8px; color: var(--title); }
  .publisher { position: absolute; right: 22px; bottom: 24px;
    font-family: "Montserrat", sans-serif; font-weight: 400;
    font-size: 20px; letter-spacing: 1px; color: var(--logo); }
</style>
</head>
<body>
<div class="canvas">

  <section class="cover cover--back">
    <div class="decor decor--corner" role="img" aria-label="Colourful star-flower ornament"></div>
    <div class="decor decor--edge" role="img" aria-label="Colourful star-flower nodes continuing from the front"></div>
    <div class="spine-line"></div>

    <div class="blurb">
      <p>Is your organization failing to create the environment where real collaboration, innovation and speed are a natural habit and people are truly engaged?</p>
      <p>What if the real key to all this was a radical change in the way your organization is actually structured?</p>
      <p>The authors’ +15year experience in change initiatives, together with the outcomes of an extensive qualitative and quantitative research, led to the creation of Brevunt. Brevunt is a revolutionary organizational model based on a radial and peer- based structure of self-organized and coordinated teams that overcome the limits of the hierarchy and expands individual, team and organizational potential.</p>
    </div>

    <div class="bio bio--first">
      <svg class="bio__photo" viewBox="0 0 86 116" role="img" aria-label="Portrait photo of Lucrezia Manfretti">
        <defs><linearGradient id="photoA" x1="0" y1="0" x2="0" y2="1">
          <stop offset="0" stop-color="#efe7e2"/><stop offset="0.6" stop-color="#e4b79a"/><stop offset="1" stop-color="#c8456a"/></linearGradient></defs>
        <rect width="86" height="116" fill="url(#photoA)"/>
      </svg>
      <p class="bio__text"><span class="bio__name">Lucrezia Manfretti</span> is a partner at Quolvane, a global organizational development firm, a former executive in the corporate setting (including Brindle &amp; Holloway and Zimbu! Inc.) and Past President of GTN Global (Global Tutoring Network). She is the author of the book “Inner Compass. The Road to Renewing Guidance” and a LUMIx speaker.</p>
    </div>

    <div class="bio bio--second">
      <svg class="bio__photo" viewBox="0 0 86 116" role="img" aria-label="Portrait photo of Marcello Vagni">
        <defs><linearGradient id="photoB" x1="0" y1="0" x2="0" y2="1">
          <stop offset="0" stop-color="#a9705a"/><stop offset="0.55" stop-color="#cfa088"/><stop offset="1" stop-color="#f2efec"/></linearGradient></defs>
        <rect width="86" height="116" fill="url(#photoB)"/>
      </svg>
      <p class="bio__text"><span class="bio__name">Marcello Vagni</span> is a partner at Quolvane and a former manager in multinational settings. He is the co-author of the Keswick Management Quarterly articles “Why Your Inner Mood Shapes your Daily Output”, “3 Ways to Lift a Gloomy Day”, “Preparing Your Thoughts Properly for a Long Break” and “An Easy Method to Ease Lasting Tension”.</p>
    </div>
  </section>

  <section class="cover cover--front">
    <div class="spine-line"></div>
    <h1 class="title">Brevunt</h1>
    <h2 class="subtitle">5 RULES TO BUILD A<br>PEOPLE-FIRST OFFICE</h2>
    <svg class="illustration" viewBox="0 0 330 368" role="img" aria-label="Illustration of five colourful star-flower nodes joined in a radial network">
      <defs><linearGradient id="network" x1="0" y1="0" x2="1" y2="1">
        <stop offset="0" stop-color="#8cc84b"/><stop offset="0.3" stop-color="#3a86c5"/>
        <stop offset="0.55" stop-color="#e83f8b"/><stop offset="0.8" stop-color="#8e3f9c"/><stop offset="1" stop-color="#f3a03a"/></linearGradient></defs>
      <rect width="330" height="368" rx="40" fill="url(#network)" opacity="0.55"/>
    </svg>
    <p class="authors">LUCREZIA MANFRETTI<br>&amp; MARCELLO VAGNI</p>
    <p class="publisher">QUOLVANE</p>
  </section>

</div>
</body>
</html>
```